label design for coffee bean packaging

Logo will be provided. Label design for package of coffee beans for a micro roasted coffee company. Need to have space to write in origin, weight with check box for 1/4, 1/2, 1lb. Need to have check boxes for Light, Medium, Dark. Creative unique label design with boarders and fun, modern design. Company name is Cedar Brook Roasting Company. See attached logo. I have source files for logo if needed for design.
Industry/Entity Type
Coffee Shop
Font styles to use
Other font styles liked:
- Montez, kautiva cyrillic, uniform bold
Colors
f78f20
faa54b
f37122
fece3e
acd036
Requirements
Must have
- logo included in the design

```html
<!DOCTYPE html>
<html lang="en">
<head>
<meta charset="utf-8">
<title>Cedar Brook Coffee Roaster – Bean Label</title>
<link rel="stylesheet" href="https://fonts.googleapis.com/css2?family=Raleway:wght@400;500&family=Satisfy&family=Dancing+Script:wght@400&display=block">
<style>
  :root {
    --paper: #ffffff;
    --roast-dark: #1f1410;
    --roast-mid: #3a2419;
    --mauve: #9a6667;
    --mauve-line: #b9807f;
    --cream: #ffffff;
    --ink-brown: #5a3325;
    --dot: #5b3a38;
  }
  * { margin: 0; padding: 0; box-sizing: border-box; }
  html, body { width: 974px; height: 1200px; overflow: hidden; background: var(--paper); }
  .label {
    position: relative; width: 974px; height: 1200px;
    font-family: "Raleway", sans-serif; color: var(--cream);
  }
  .bean-backdrop {
    position: absolute; left: 35px; top: 35px; width: 903px; height: 1128px;
    background: radial-gradient(ellipse at 50% 45%, var(--roast-mid) 0%, var(--roast-dark) 80%);
  }
  .frame { position: absolute; left: 0; top: 0; }
  .brand-seal {
    position: absolute; left: 358px; top: 172px; width: 258px; height: 258px;
    border-radius: 50%; background: var(--paper);
    display: flex; align-items: center; justify-content: center; text-align: center;
    padding: 30px;
  }
  .brand-seal__name {
    font-family: "Raleway", sans-serif; font-weight: 500; font-size: 28px;
    line-height: 1.25; color: var(--ink-brown);
  }
  .title {
    position: absolute; left: 130px; width: 714px; top: 500px; text-align: center;
    font-family: "Satisfy", "Dancing Script", cursive; font-weight: 400;
    font-size: 68px; line-height: 1.1; white-space: nowrap; overflow: hidden;
    color: var(--cream);
  }
  .details-band {
    position: absolute; left: 35px; top: 673px; width: 903px; height: 287px;
    background: var(--mauve);
  }
  .field-label { position: absolute; font-size: 26.5px; font-weight: 400; }
  .dots-h { position: absolute; border-top: 2px dotted var(--dot); height: 0; }
  .dots-v { position: absolute; border-left: 2px dotted var(--dot); width: 0; }
  .check { position: absolute; display: flex; align-items: center; gap: 6px; font-size: 30px; }
  .check__box { width: 22px; height: 22px; border: 2px solid var(--cream); display: inline-block; }
  .roast-level { position: absolute; top: 1012px; left: 0; width: 974px; }
  .roast-level .check { font-size: 34px; letter-spacing: 0.5px; }
  .roast-level .check__box { width: 24px; height: 24px; }
  .web {
    position: absolute; left: 0; width: 974px; top: 1093px; text-align: center;
    font-size: 26.5px; color: var(--mauve-line);
  }
</style>
</head>
<body>
<div class="label">
  <div class="bean-backdrop" role="img" aria-label="Close-up photograph of dark roasted coffee beans"></div>

  <svg class="frame" width="974" height="1200" viewBox="0 0 974 1200" fill="none" stroke="var(--mauve-line)" stroke-width="2">
    <path d="M265 1120 H120 A40 40 0 0 0 80 1080 V118 A40 40 0 0 0 120 78 H854 A40 40 0 0 0 894 118 V1080 A40 40 0 0 0 854 1120 H712"/>
  </svg>

  <div class="brand-seal">
    <span class="brand-seal__name">Cedar Brook Roasting Company</span>
  </div>

  <h1 class="title">Cedar Brook Coffee Roaster</h1>

  <div class="details-band"></div>
  <span class="field-label" style="left:175px; top:712px;">County of Origin / Appellation</span>
  <div class="dots-h" style="left:175px; top:790px; width:460px;"></div>
  <div class="dots-v" style="left:678px; top:735px; height:200px;"></div>
  <div class="dots-v" style="left:390px; top:815px; height:120px;"></div>
  <span class="field-label" style="left:175px; top:855px;">Estate / Farm</span>
  <div class="dots-h" style="left:175px; top:928px; width:180px;"></div>
  <span class="field-label" style="left:430px; top:855px;">Date Roasted</span>
  <div class="dots-h" style="left:430px; top:928px; width:198px;"></div>

  <div class="check" style="left:725px; top:762px;"><span class="check__box"></span>1/4</div>
  <div class="check" style="left:725px; top:834px;"><span class="check__box"></span>1.2</div>
  <div class="check" style="left:725px; top:897px;"><span class="check__box"></span>1lb</div>

  <div class="roast-level">
    <div class="check" style="left:215px;"><span class="check__box"></span>LIGHT</div>
    <div class="check" style="left:400px;"><span class="check__box"></span>MEDIUM</div>
    <div class="check" style="left:625px;"><span class="check__box"></span>DARK</div>
  </div>

  <p class="web">www.cedarbrookroastingco.com</p>
</div>
</body>
</html>
```